Weekly Newsletter template for our niche within the Telecom Industry

We need a 'skeleton' format where we can insert our weekly information and ads.
We will do all the content in-house.
Content in both info and ads must be able to contain hyperlinks.
Our company website is: www. halverly-dunmoor.com
We think we would like something similar to the top format but with the single bar on the right side as a place to insert ads
Thank you.

```html
<!DOCTYPE html>
<html lang="en">
<head>
<meta charset="utf-8">
<title>Halverly Dunmoor Weekly Newsletter</title>
<link rel="stylesheet" href="https://fonts.googleapis.com/css2?family=Poppins:wght@400;500;600;700&family=Roboto:wght@300;400;700&display=swap">
<style>
  :root {
    --backdrop: #d3d3d3;
    --paper: #ffffff;
    --sky: #e2f4f9;
    --teal: #1fb5d2;
    --lime: #b7cf3f;
    --ink: #2e2e2e;
    --ink-soft: #4a4a4a;
    --bar: #2f2f2f;
  }
  * { box-sizing: border-box; margin: 0; padding: 0; }
  html, body { width: 1038px; height: 1200px; overflow: hidden; background: var(--backdrop); }
  body { font-family: "Poppins", sans-serif; color: var(--ink); }
  .page {
    position: absolute; left: 95px; top: 0; width: 848px; height: 1200px;
    background: var(--paper); overflow: hidden;
  }
  .masthead-band { position: absolute; left: 0; top: 0; width: 100%; height: 360px; background: var(--sky); }

  .brand { position: absolute; left: 45px; top: 62px; display: flex; align-items: center; gap: 12px; }
  .brand-dot { width: 44px; height: 44px; border-radius: 50%; background: var(--teal); }
  .brand-name { font-weight: 600; font-size: 19px; letter-spacing: 0.5px; color: var(--ink); line-height: 1; }

  .feature-box {
    position: absolute; left: 40px; top: 133px; width: 312px; height: 472px;
    background: var(--teal); color: #fff; padding: 32px 22px 0 30px;
  }
  .feature-title { font-weight: 600; font-size: 27px; line-height: 1.2; margin-bottom: 14px; }
  .feature-text { font-size: 15px; line-height: 22.8px; }
  .feature-text a { color: inherit; text-decoration: none; }

  .read-more {
    position: absolute; right: 0; bottom: 0; width: 107px; height: 23px;
    background: var(--bar); color: #fff; font-size: 11.5px; line-height: 24px;
    text-align: center; text-decoration: none;
  }
  .ad-slot { position: absolute; left: 40px; width: 312px; height: 259px; }
  .ad-slot.first { top: 611px; background: radial-gradient(circle at 57% 36%, #6fd8ff 0%, #1a84d6 28%, #0c4f9a 62%, #08335f 100%); }
  .ad-slot.second { top: 875px; background: linear-gradient(120deg, #c9def6 0%, #9cc0ec 45%, #6e98d4 78%, #4c6e9e 100%); }

  .issue { position: absolute; left: 388px; width: 420px; }
  .issue-date { top: 88px; font-size: 18px; color: var(--ink-soft); }
  .issue-title {
    top: 120px; font-family: "Roboto", sans-serif; font-weight: 700;
    font-size: 56px; line-height: 58px; color: var(--ink); letter-spacing: -0.3px;
  }
  .issue-sub {
    top: 301px; font-family: "Roboto", sans-serif; font-weight: 400;
    font-size: 30px; color: var(--teal); line-height: 1;
  }

  .accent-rule { position: absolute; left: 391px; top: 424px; width: 86px; height: 8px; background: linear-gradient(90deg, var(--teal), var(--lime)); }
  .story { position: absolute; left: 388px; width: 402px; }
  .story-title { top: 448px; font-weight: 600; font-size: 33px; line-height: 34px; }
  .sub-heading { font-weight: 700; font-size: 16.5px; text-transform: uppercase; margin-bottom: 3px; }
  .body-text { font-size: 14.3px; line-height: 17px; color: var(--ink); margin-bottom: 6px; }
  .body-text.strong { font-weight: 600; }
  .body-text a { color: inherit; }
  .section-one { top: 542px; }
  .pull-quote {
    top: 816px; height: 64px; border-top: 1.5px solid var(--teal); border-bottom: 1.5px solid var(--teal);
    color: var(--teal); font-weight: 600; font-size: 14.3px; line-height: 17px; padding-top: 12px;
  }
  .section-two { top: 899px; }
  .section-two .body-text { line-height: 19px; }
  .section-three { top: 1006px; }
  .section-three .body-text { line-height: 20px; margin-bottom: 12px; }
  .checklist { list-style: none; }
  .checklist li { display: flex; align-items: center; gap: 12px; font-size: 14.3px; line-height: 23px; }
  .checklist svg { width: 13px; height: 13px; flex: none; }

  .site-link { position: absolute; left: 40px; top: 1161px; display: flex; align-items: center; gap: 5px; font-size: 10.5px; color: var(--ink-soft); text-decoration: none; }
  .site-link svg { width: 14px; height: 14px; }
  .foot-bar { position: absolute; left: 0; bottom: 0; width: 100%; height: 10px; background: var(--bar); }
</style>
</head>
<body>
<main class="page">
  <div class="masthead-band"></div>

  <div class="brand">
    <span class="brand-dot"></span>
    <span class="brand-name">HALVERLY DUNMOOR</span>
  </div>

  <section class="feature-box">
    <h2 class="feature-title">Hedding</h2>
    <p class="feature-text">explabora corehenda dolum si occatem accum nim rae velitibus et reped qui ommo optati simusa quam de dolessi bla verrore mpore, que nonse exerit autat estiunt andelestis voluptamus dunt excerios aut ommolest Citaerferrunt ad ut laturit emolore henestias doluptam ipid utemquae et fuga. Ut et a et evelit labo. Enisti ra cus eaque perem que preratqui ad ut eum faccabo. Tis est porum essinte necus.<br>Usa volut quam lautaquibus et, sectore vel inihil ipis exercit</p>
    <a class="read-more" href="#">Read More...</a>
  </section>

  <div class="ad-slot first" role="img" aria-label="Photo of a hand touching a glowing blue AI circuit interface">
    <a class="read-more" href="#">Read More...</a>
  </div>
  <div class="ad-slot second" role="img" aria-label="Photo of a telecom transmission tower with signal waves on a blue bokeh sky">
    <a class="read-more" href="#">Read More...</a>
  </div>

  <p class="issue issue-date">Date | Month</p>
  <h1 class="issue issue-title">YOUR<br>COMPANY<br>NEWS LETTER</h1>
  <p class="issue issue-sub">WEEKLY UPDATE</p>

  <div class="accent-rule"></div>
  <h2 class="story story-title">This is Heading This is Heading</h2>

  <article class="story section-one">
    <h3 class="sub-heading">This is sub heading</h3>
    <p class="body-text">Iliquiat urepedi volorrovitia voluptae perovita volupti usdant verum dit dolest laciam eria sent ra doluptaspit rerferum repudip icium, simporiorem rem evel invendigene diae nusa sim quate nis ditatibus samus</p>
    <p class="body-text strong">excessus voluptae verum fugit ipsapit ute volo mo tore sitatendit alicius doluptaqui doluptatio.</p>
    <p class="body-text">usdant verum dit dolest laciam eria sent ra doluptaspit rerferum repudip icium, simporiorem rem evel</p>
    <p class="body-text strong">excessus voluptae verum fugit ipsapit ute volo mo tore sitatendit alicius doluptaqui doluptatio.</p>
    <p class="body-text">usdant verum dit dolest laciam eria sent ra doluptaspit rerferum repudip icium, simporiorem rem evel</p>
  </article>

  <blockquote class="story pull-quote">usdant verum dit dolest laciam eria sent ra doluptaspit rerferum repudip icium, simporiorem rem evel</blockquote>

  <article class="story section-two">
    <h3 class="sub-heading">This is sub heading</h3>
    <p class="body-text">Iliquiat urepedi volorrovitia voluptae perovita volupti usdant verum dit dolest laciam eria sent ra doluptaspit rerferum repudip icium, simporiorem rem evel</p>
  </article>

  <article class="story section-three">
    <h3 class="sub-heading">This is sub heading</h3>
    <p class="body-text">Et maximinis as della et aut et quia doluptae quis molendi tiuntur,</p>
    <ul class="checklist">
      <li><svg viewBox="0 0 16 16"><circle cx="8" cy="8" r="8" fill="#1fb5d2"/><path d="M4.5 8.3l2.3 2.3 4.7-4.8" fill="none" stroke="#fff" stroke-width="1.8" stroke-linecap="round" stroke-linejoin="round"/></svg>Verempo reptatet: magnis asi cus alitas</li>
      <li><svg viewBox="0 0 16 16"><circle cx="8" cy="8" r="8" fill="#1fb5d2"/><path d="M4.5 8.3l2.3 2.3 4.7-4.8" fill="none" stroke="#fff" stroke-width="1.8" stroke-linecap="round" stroke-linejoin="round"/></svg>Verempo reptatet: magnis asi cus alitas</li>
    </ul>
  </article>

  <a class="site-link" href="#">
    <svg viewBox="0 0 16 16" fill="none" stroke="#1fb5d2" stroke-width="1.2"><circle cx="8" cy="8" r="7"/><ellipse cx="8" cy="8" rx="3" ry="7"/><path d="M1 8h14M2.2 4.5h11.6M2.2 11.5h11.6"/></svg>
    www. halverly-dunmoor.com
  </a>
  <div class="foot-bar"></div>
</main>
</body>
</html>
```